Velbrix SA

Découpe de métaux - Fourniture de tôles - Accessoires de machines de chantier (European Patent)

Les designs se ressemblent

Besoin de plus de jours pour examiner

• Mon projet doit comprendre la photo de la halle (bâtiment)

```html
<!DOCTYPE html>
<html lang="fr">
<head>
<meta charset="utf-8">
<title>Velbrix SA – Découpe de métaux</title>
<link rel="stylesheet" href="https://fonts.googleapis.com/css2?family=Fira+Sans+Condensed:ital,wght@1,800&family=Roboto+Condensed:ital,wght@0,400;1,400&display=swap">
<style>
  :root {
    --page-bg: #d9d9db;
    --brand-blue: #1f56b8;
    --brand-blue-light: #2f6cd0;
    --brand-red: #e3262b;
    --panel-black: #050505;
    --panel-grey: #2b2b30;
    --paper: #ffffff;
    --photo-dark: #3f3d4c;
    --photo-mid: #77718c;
    --photo-light: #d6d0e4;
    --photo-glow: #f4eefc;
  }
  * { margin: 0; padding: 0; box-sizing: border-box; }
  html, body {
    width: 1200px;
    height: 1200px;
    overflow: hidden;
    background: var(--page-bg);
  }
  .flyer {
    position: absolute;
    left: 78px;
    top: 225px;
    width: 1044px;
    height: 750px;
    display: block;
  }
  .headline {
    font-family: "Fira Sans Condensed", "Arial Narrow", sans-serif;
    font-style: italic;
    font-weight: 800;
    font-size: 73px;
    fill: var(--paper);
  }
  .service-line, .footer-url, .brand-name {
    font-family: "Roboto Condensed", "Arial Narrow", sans-serif;
    font-weight: 400;
    fill: var(--paper);
  }
  .service-line { font-size: 34px; }
  .footer-url { font-size: 40px; fill: var(--paper); }
  .brand-name { font-size: 44px; }
  .patent-note {
    font-family: "Roboto Condensed", "Arial Narrow", sans-serif;
    font-style: italic;
    font-size: 31px;
    fill: var(--paper);
  }
</style>
</head>
<body>
<svg class="flyer" viewBox="0 0 957 687" xmlns="http://www.w3.org/2000/svg">
  <defs>
    <linearGradient id="header-gradient" x1="0" y1="0" x2="0" y2="1">
      <stop offset="0" stop-color="var(--brand-blue-light)"/>
      <stop offset="1" stop-color="var(--brand-blue)"/>
    </linearGradient>
    <linearGradient id="photo-gradient" x1="0" y1="0" x2="1" y2="1">
      <stop offset="0" stop-color="var(--photo-dark)"/>
      <stop offset="0.4" stop-color="var(--photo-mid)"/>
      <stop offset="0.75" stop-color="var(--photo-light)"/>
      <stop offset="1" stop-color="#8f8aa3"/>
    </linearGradient>
    <radialGradient id="photo-glow" cx="330" cy="520" r="230" gradientUnits="userSpaceOnUse">
      <stop offset="0" stop-color="var(--photo-glow)" stop-opacity="0.9"/>
      <stop offset="1" stop-color="var(--photo-glow)" stop-opacity="0"/>
    </radialGradient>
    <linearGradient id="stripe-gradient" x1="0" y1="1" x2="1" y2="0">
      <stop offset="0" stop-color="var(--brand-blue)"/>
      <stop offset="1" stop-color="#6a4f9a"/>
    </linearGradient>
  </defs>

  <rect class="flyer-paper" width="957" height="687" fill="var(--paper)"/>

  <g class="hero-photo" role="img" aria-label="Photo: tête de découpe plasma d'une machine CNC découpant une tôle d'acier dans la halle de production">
    <rect x="0" y="117" width="957" height="509" fill="url(#photo-gradient)"/>
    <rect x="0" y="117" width="957" height="509" fill="url(#photo-glow)"/>
  </g>

  <polygon class="header-band" points="0,0 928,0 830,114 0,114" fill="url(#header-gradient)"/>
  <line class="header-rule" x1="0" y1="54" x2="103" y2="54" stroke="var(--paper)" stroke-width="3"/>
  <text class="headline" x="117" y="88" textLength="633" lengthAdjust="spacingAndGlyphs">DÉCOUPE DE MÉTAUX</text>

  <polygon class="corner-red-stripe" points="928,0 957,0 957,12 845,141 812,141" fill="var(--brand-red)"/>
  <polygon class="info-panel" points="957,12 957,687 495,687 800,314 845,141" fill="var(--panel-black)"/>
  <polygon class="white-stripe" points="455,687 495,687 800,314 760,314" fill="var(--paper)"/>
  <polygon class="blue-stripe" points="420,687 455,687 760,314 725,350" fill="url(#stripe-gradient)"/>
  <polygon class="red-wedge" points="628,316 705,316 655,374" fill="var(--brand-red)"/>

  <polygon class="brand-panel" points="700,141 957,141 957,316 628,316" fill="var(--panel-grey)"/>
  <text class="brand-name" x="822" y="244" text-anchor="middle">Velbrix SA</text>

  <rect class="footer-strip" x="0" y="626" width="440" height="61" fill="var(--paper)"/>
  <polygon class="footer-band" points="118,630 460,630 425,687 85,687" fill="var(--brand-blue)"/>
  <g class="globe-icon" fill="none" stroke="var(--brand-red)" stroke-width="2.5">
    <circle cx="45" cy="658" r="15"/>
    <ellipse cx="45" cy="658" rx="6" ry="15"/>
    <line x1="30" y1="658" x2="60" y2="658"/>
  </g>
  <text class="footer-url" x="122" y="673">VELBRIX.CH</text>

  <g class="service-list">
    <polygon class="bullet" points="738,456 750,466 738,476" fill="var(--brand-red)"/>
    <text class="service-line" x="941" y="478" text-anchor="end">FOURNITURE</text>
    <text class="service-line" x="941" y="519" text-anchor="end">DE TÔLES</text>
    <polygon class="bullet" points="677,543 689,553 677,563" fill="var(--brand-red)"/>
    <text class="service-line" x="941" y="565" text-anchor="end">ACCESSOIRES DE</text>
    <text class="service-line" x="941" y="606" text-anchor="end">MACHINES DE CHANTIER</text>
  </g>
  <line class="service-rule" x1="588" y1="625" x2="957" y2="625" stroke="var(--brand-red)" stroke-width="3"/>
  <text class="patent-note" x="941" y="668" text-anchor="end">(EUROPEAN PATENT)</text>
</svg>
</body>
</html>
```